New retail box design

We are looking at changing our packaging for retilers. I have templates of boxes and like a great design for new packaging.

I will attach pictures of our current packaging.

Industry/Entity Type

Ammunition manufacturing

Requirements
Must have
• warning label and company name

```html
<!DOCTYPE html>
<html lang="en">
<head>
<meta charset="utf-8">
<title>Retail Box Packaging</title>
<link rel="stylesheet" href="https://fonts.googleapis.com/css2?family=Inter:wght@700&family=Roboto+Condensed:wght@400;700&display=swap">
<style>
  :root {
    --bg: #f6f6f6;
    --panel: #f2f2f2;
    --panel-side: #e9e9ea;
    --edge: #d8d8da;
    --navy: #2f3d78;
    --navy-dark: #24305f;
    --red: #b3252c;
    --cream: #efe9e2;
    --ink: #333640;
    --warn: #2a9fd6;
    --name: #334066;
    --gun: #2a2a2c;
    --brass: #c89a3c;
  }
  html, body {
    margin: 0;
    padding: 0;
    width: 1200px;
    height: 1109px;
    overflow: hidden;
    background: var(--bg);
  }
  .canvas {
    position: relative;
    width: 1200px;
    height: 1109px;
  }
  .panel {
    position: absolute;
    box-sizing: border-box;
    border: 1px solid var(--edge);
  }
  .panel--top {
    left: 440px; top: 90px; width: 660px; height: 200px;
    background: var(--panel);
  }
  .panel--side {
    left: 80px; top: 290px; width: 360px; height: 660px;
    background: var(--panel-side);
    font-family: "Roboto Condensed", sans-serif;
    color: var(--ink);
  }
  .panel--front {
    left: 440px; top: 290px; width: 660px; height: 660px;
    background: var(--panel);
    overflow: hidden;
  }
  .top-emblem {
    position: absolute;
    left: 150px; top: 40px; width: 360px; height: 120px;
    background: linear-gradient(90deg, var(--navy) 0%, var(--navy-dark) 55%, var(--red) 100%);
    opacity: .85;
    border-radius: 4px;
  }
  .warning {
    position: absolute;
    left: 24px; top: 26px;
    margin: 0;
    font-size: 24px;
    color: var(--warn);
    font-weight: 400;
  }
  .safety {
    position: absolute;
    left: 24px; top: 200px; right: 24px;
  }
  .safety-title {
    margin: 0 0 18px;
    font-size: 17px;
    font-weight: 700;
  }
  .safety-list {
    margin: 0;
    padding-left: 18px;
    font-size: 16px;
    line-height: 1.35;
    list-style: square;
  }
  .flag-art {
    position: absolute;
    left: 0; top: 0; width: 300px; height: 660px;
    clip-path: polygon(0 0, 100% 0, 95% 30%, 80% 60%, 55% 100%, 0 100%);
    background: linear-gradient(180deg, var(--navy) 0%, var(--navy) 55%, var(--cream) 68%, var(--red) 85%, #8a1c22 100%);
  }
  .brand {
    position: absolute;
    right: 48px; top: 70px;
    width: 220px;
    text-align: center;
  }
  .brand-mark {
    display: block;
    width: 40px; height: 40px;
    margin: 0 auto 18px;
    background: var(--navy);
  }
  .brand-name {
    margin: 0;
    font-family: "Inter", sans-serif;
    font-weight: 700;
    font-size: 34px;
    line-height: 1.3;
    color: var(--name);
  }
  .product-art {
    position: absolute;
    left: 370px; top: 390px; width: 250px; height: 170px;
    background: linear-gradient(135deg, #4a4a4e 0%, var(--gun) 60%, var(--brass) 100%);
    border-radius: 6px;
  }
  .corner-emblem {
    position: absolute;
    left: 930px; top: 880px; width: 230px; height: 200px;
    background: linear-gradient(135deg, var(--navy) 0%, var(--navy-dark) 55%, var(--red) 100%);
    border-radius: 6px;
    opacity: .9;
  }
</style>
</head>
<body>
<main class="canvas">
  <section class="panel panel--top">
    <div class="top-emblem" role="img" aria-label="Illustration of an eagle in flight over a waving American flag"></div>
  </section>

  <section class="panel panel--side">
    <p class="warning">Warning: Keep out of reach of children.</p>
    <div class="safety">
      <h2 class="safety-title">Safety Rules:</h2>
      <ul class="safety-list">
        <li>Watch your muzzle. Keep gun pointed in safe direction.</li>
        <li>Wear eye and ear protection.</li>
        <li>If gun fails to fire, keep it pointed in a safe direction, then unload carefully avoiding exposure to breech.</li>
        <li>Know your target and what is beyond it.</li>
        <li>Treat every gun as if it were loaded. Don't rely on the safety.</li>
        <li>Keep barrel clear of obstructions.</li>
        <li>Never load a gun until ready to use.</li>
        <li>Only use ammunition that extractly matches marking of your gun.</li>
      </ul>
    </div>
  </section>

  <section class="panel panel--front">
    <div class="flag-art" role="img" aria-label="Photograph of a draped American flag with stars and stripes"></div>
    <div class="brand">
      <span class="brand-mark"></span>
      <h1 class="brand-name">Company<br>Name</h1>
    </div>
    <div class="product-art" role="img" aria-label="Illustration of a black pistol with three brass bullets"></div>
  </section>

  <div class="corner-emblem" role="img" aria-label="Illustration of an eagle in flight over a waving American flag"></div>
</main>
</body>
</html>
```